BOLD & MINIMALIST DESIGN NEEDED

We want a very bold but minimalistic business card design that is impactful and utilizes both sides of the business card. Our current logo is included for your use.

We want bold fonts and good use of negative space. We don't want the logo to overpower the design.

Target Market(s)

Professionals who are building new commercial buildings.

Industry/Entity Type

Construction

Contact Information for Business Card

Name, Title, email, office phone, cell phone, website

Font styles to use
Serif
Sans Serif

Requirements
Must have
• Bold design!

```html
<!DOCTYPE html>
<html lang="en">
<head>
<meta charset="utf-8">
<title>Ridgeline Design + Build – Business Card</title>
<link href="https://fonts.googleapis.com/css2?family=Montserrat:wght@400;500;700&display=swap" rel="stylesheet">
<style>
  :root {
    --stage: #ececec;
    --paper: #ffffff;
    --ink: #111111;
    --lime: #a8d16b;
  }
  html, body {
    margin: 0;
    padding: 0;
    width: 1200px;
    height: 1200px;
    overflow: hidden;
    background: var(--stage);
  }
  .canvas {
    position: relative;
    width: 1200px;
    height: 1200px;
  }
  .card {
    position: absolute;
    left: 162px;
    width: 875px;
    height: 512.5px;
    background: var(--paper);
  }
  .card--front { top: 71px; }
  .card--back { top: 615px; }
  .card svg {
    display: block;
    width: 100%;
    height: 100%;
  }
  .fill-lime { fill: var(--lime); }
  .fill-ink { fill: var(--ink); }
  .client-name {
    font-family: "Montserrat", sans-serif;
    font-weight: 700;
    font-size: 28px;
    fill: var(--ink);
  }
  .client-role {
    font-family: "Montserrat", sans-serif;
    font-weight: 500;
    font-size: 19px;
    fill: var(--ink);
  }
  .contact-line {
    font-family: "Montserrat", sans-serif;
    font-weight: 500;
    font-size: 17px;
    fill: var(--ink);
  }
  .brand-name {
    font-family: "Montserrat", sans-serif;
    font-weight: 700;
    fill: var(--ink);
  }
</style>
</head>
<body>
<main class="canvas">

  <section class="card card--front" aria-label="Business card front">
    <svg viewBox="0 0 700 410" xmlns="http://www.w3.org/2000/svg">
      <polygon class="fill-lime" points="0,222 320,222 460,410 0,410"/>
      <polygon class="fill-ink" points="338,222 350,222 490,410 478,410"/>

      <g class="brand-lockup">
        <rect class="fill-lime" x="527" y="100" width="30" height="30"/>
        <text class="brand-name" x="542" y="176" font-size="40" text-anchor="middle">RIDGELINE</text>
        <text class="brand-name" x="542" y="198" font-size="14" letter-spacing="4" text-anchor="middle">DESIGN + BUILD</text>
      </g>

      <text class="client-name" x="48" y="148">CLIENT NAME</text>
      <text class="client-role" x="48" y="175">Designation</text>

      <g class="contact-list">
        <path class="fill-ink" d="M48 255 l3 -1 l2 4 l-2 1.5 q1.5 3 4.5 4.5 l1.5 -2 l4 2 l-1 3 q-8 0 -12 -12z"/>
        <text class="contact-line" x="77" y="268">555-555-5555</text>

        <rect class="fill-ink" x="50" y="288" width="8" height="13" rx="1.5"/>
        <rect x="52" y="290" width="4" height="8" fill="var(--lime)"/>
        <text class="contact-line" x="77" y="300">6500 412 730</text>

        <rect class="fill-ink" x="48" y="323" width="12" height="9"/>
        <path d="M48 323 l6 5 l6 -5" fill="none" stroke="var(--lime)" stroke-width="1.3"/>
        <text class="contact-line" x="77" y="332">email@ridgeline.com</text>

        <circle cx="54" cy="360" r="5.5" fill="none" stroke="var(--ink)" stroke-width="1.6"/>
        <path d="M48.5 360 h11 M54 354.5 v11" stroke="var(--ink)" stroke-width="1.2"/>
        <text class="contact-line" x="77" y="364">www.ridgeline.com</text>
      </g>
    </svg>
  </section>

  <section class="card card--back" aria-label="Business card back">
    <svg viewBox="0 0 700 410" xmlns="http://www.w3.org/2000/svg">
      <polygon class="fill-lime" points="0,0 700,0 700,64 0,26"/>
      <polygon class="fill-ink" points="0,40 700,80 700,90 0,52"/>

      <g class="brand-lockup">
        <rect class="fill-lime" x="332" y="200" width="36" height="36"/>
        <text class="brand-name" x="350" y="318" font-size="52" text-anchor="middle">RIDGELINE</text>
        <text class="brand-name" x="350" y="346" font-size="17" letter-spacing="5" text-anchor="middle">DESIGN + BUILD</text>
      </g>
    </svg>
  </section>

</main>
</body>
</html>
```